Pelican Global Trade & Heritage Forum Landing Page Design

We are a Chinese high-end bespoke business travel company. We want to design a landing page, to promote our brand and business, to attract target clients for business development.

We have own logo, like design in modern simple style, like to sample as attached. Like the Sample 2, use different color to display our business services.

We want to mainly display 7 parts of business:
1. Visa Services
2. International Hotel Reservation
3. Worldwide Flight Tickets Booking
4. Worldwide Travel Arrangement
5. VIP Airport Concierge
6. Duty Free Goods
7. International Business Resources

We imagine design a world map, points out popular countries, cities, and destinations, and combine with our own business resources cities.

Design in modern, business, international style. Thank you. Look forward to cooperate with you.

Target Market(s)

Business Clients and High income private client

Industry/Entity Type

Tourism, Business Travel, International Exchange

Coding

Coded - Design and coding required

Requirements
Must have
• Our logo, large images, design a world map

```html
<!DOCTYPE html>
<html lang="en">
<head>
<meta charset="utf-8">
<title>Pelican Global Trade &amp; Heritage Forum</title>
<link href="https://fonts.googleapis.com/css2?family=Exo+2:wght@500;600;700;800&family=Roboto:wght@300;400;500&display=swap" rel="stylesheet">
<style>
:root{
  --navy:#0d2f8a;
  --deep:#0a2a8c;
  --btn:#1b4c9e;
  --orange:#f07a1a;
  --yellow:#f3bf2a;
  --lime:#a3cf1c;
  --teal:#5ccdb2;
  --cyan:#1fa6d6;
  --blue:#2a72d6;
  --royal:#0f46b0;
  --grey:#f4f4f4;
  --text:#555;
  --dark:#222;
}
*{margin:0;padding:0;box-sizing:border-box}
html,body{width:1200px;height:3992px;overflow:hidden;background:#fff}
body{position:relative;font-family:'Roboto',sans-serif;color:var(--text)}

/* header */
.site-header{position:absolute;left:0;top:0;width:1200px;height:114px;background:#fff}
.brand{position:absolute;left:100px;top:32px;width:300px;display:flex;align-items:center;gap:12px;font-family:'Exo 2',sans-serif;font-weight:700;font-size:18px;line-height:22px;color:var(--navy)}
.brand-dot{width:40px;height:40px;border-radius:50%;background:var(--navy);flex:none}
.nav{position:absolute;top:55px;left:0;font-family:'Exo 2',sans-serif;font-weight:700;font-size:15px;color:var(--navy)}
.nav a{position:absolute;white-space:nowrap;text-decoration:none;color:inherit}
.btn{display:inline-flex;align-items:center;justify-content:center;background:var(--btn);color:#fff;font-family:'Exo 2',sans-serif;font-weight:700;font-size:15px;border-radius:5px;text-decoration:none}

/* hero */
.hero{position:absolute;left:0;top:114px;width:1200px;height:631px;background:linear-gradient(100deg,#8fa3bd 0%,#c9c4bd 35%,#f2a35a 55%,#e86b1d 75%,#5a3a2a 100%)}
.hero-title{position:absolute;left:197px;top:130px;font-family:'Exo 2',sans-serif;font-weight:800;color:var(--navy);font-size:60px;line-height:66px}
.hero-title span{display:block;font-size:52px}
.hero .btn{position:absolute;left:197px;top:268px;width:127px;height:45px}

/* services */
.section-title{position:absolute;left:0;width:1200px;text-align:center;font-family:'Exo 2',sans-serif;font-weight:800;font-size:40px;color:var(--navy)}
.mark{position:absolute;border-radius:50%}
.hex{position:absolute}
.svc{position:absolute;width:180px;font-size:12px;line-height:16px;color:var(--text)}
.svc h3{font-family:'Exo 2',sans-serif;font-weight:700;font-size:17px;line-height:16px;margin-bottom:8px}
.svc.r{text-align:right}
.svc.c{text-align:center}

/* about */
.about{position:absolute;left:0;top:1676px;width:1200px;height:617px;background:var(--grey)}
.about-photo{position:absolute;left:137px;top:109px;width:400px;height:400px;border-radius:50%;background:linear-gradient(135deg,#d8dde3,#9ea6ae 55%,#4a4f57)}
.ring{position:absolute;border-radius:50%;border:2px solid}
.about h2{position:absolute;left:577px;top:130px;font-family:'Exo 2',sans-serif;font-weight:800;font-size:42px;line-height:42px;color:var(--navy)}
.grad-text{background:linear-gradient(90deg,var(--orange),var(--yellow) 50%,var(--teal));-webkit-background-clip:text;background-clip:text;color:transparent}
.about p{position:absolute;left:580px;top:232px;width:465px;font-size:13px;line-height:20.5px;color:var(--text)}
.about .btn{position:absolute;left:580px;top:438px;width:127px;height:45px}

/* news */
.card{position:absolute;top:2492px;width:347px;height:484px;border:1px solid #ddd;background:#fff}
.card-photo{height:255px}
.card h4{margin:38px 30px 0;font-weight:400;font-size:21px;line-height:28px;color:var(--dark)}
.card p{margin:14px 32px 0;font-size:13px;line-height:18px;color:#999}
.date{display:inline-block;margin:16px 30px 0;padding:4px 11px;border-radius:5px;background:linear-gradient(90deg,#e0b81c,#7cc64a,#22b5a0);color:#fff;font-family:'Exo 2',sans-serif;font-weight:700;font-size:13px}

/* cities */
.cities{position:absolute;left:0;top:3095px;width:1200px;height:485px;background:var(--deep)}
.cities h2{position:absolute;left:150px;top:152px;font-family:'Exo 2',sans-serif;font-weight:800;font-size:38px;line-height:42px;color:#fff}
.cities p{position:absolute;left:152px;top:252px;width:390px;font-size:12.5px;line-height:16px;color:#fff}
.world-map{position:absolute;left:540px;top:100px;width:635px;height:290px;border-radius:40px;background:linear-gradient(90deg,#e8b383 0%,#e1b88a 40%,#c6d796 60%,#9cd0a0 100%);opacity:.95}

/* footer */
.footer{position:absolute;left:0;top:3580px;width:1200px;height:412px;background:#fff}
.vline{position:absolute;top:10px;width:1px;height:325px;background:#ddd}
.footer h5{position:absolute;font-family:'Exo 2',sans-serif;font-weight:600;font-size:18px;color:#333}
.flinks{position:absolute;left:412px;top:120px;list-style:none;font-size:13px;line-height:26px;color:#333}
.contact-row{position:absolute;left:548px;display:flex;gap:14px;font-size:13px;line-height:17px;color:#333}
.ic{width:40px;height:40px;border-radius:50%;background:var(--btn);border:3px solid #c9d6ee;flex:none;display:flex;align-items:center;justify-content:center}
.news-txt{position:absolute;left:826px;top:118px;width:230px;font-size:13px;line-height:20px;color:#333}
.email{position:absolute;left:830px;top:176px;width:240px;height:46px;border-radius:23px;background:#f3f3f3;font-size:14px;color:#555;padding:14px 18px}
.signup{position:absolute;left:833px;top:236px;width:124px;height:38px;border-radius:19px}
.hline{position:absolute;left:138px;top:330px;width:924px;height:1px;background:#ccc}
.copy{position:absolute;left:0;top:367px;width:1200px;text-align:center;font-size:12px;color:#333}
</style>
</head>
<body>

<header class="site-header">
  <div class="brand"><span class="brand-dot"></span><span>Pelican Global Trade &amp;<br>Heritage Forum</span></div>
  <nav class="nav">
    <a style="left:455px">HOME</a>
    <a style="left:543px">ABOUT US</a>
    <a style="left:660px">SERVICES</a>
    <a style="left:773px">CLIENTS</a>
    <a style="left:877px">CONTACT</a>
  </nav>
  <a class="btn" style="position:absolute;left:978px;top:37px;width:127px;height:47px">BOOKINGS</a>
</header>

<section class="hero">
  <div role="img" aria-label="Traveller with suitcase watching a plane take off through airport terminal windows at sunset" style="position:absolute;inset:0"></div>
  <h1 class="hero-title">PELICAN GLOBAL<span>TRADE &amp; HERITAGE FORUM</span></h1>
  <a class="btn">BOOK NOW</a>
</section>

<section class="services">
  <div class="mark" style="left:578px;top:822px;width:44px;height:44px;background:var(--navy)"></div>
  <h2 class="section-title" style="top:878px">OUR SERVICES</h2>

  <svg class="hex" style="left:453px;top:972px" width="280" height="312" viewBox="0 0 280 312">
    <defs><linearGradient id="gc" x1="0" y1="0" x2="0" y2="1"><stop offset="0" stop-color="#f7f7f7"/><stop offset="1" stop-color="#d8d8d8"/></linearGradient></defs>
    <polygon points="140,6 274,82 274,230 140,306 6,230 6,82" fill="url(#gc)" stroke="#e3e3e3" stroke-width="8" stroke-linejoin="round"/>
    <circle cx="140" cy="156" r="70" fill="none" stroke="#9ccf6a" stroke-width="5"/>
  </svg>

  <svg width="0" height="0" style="position:absolute">
    <defs>
      <linearGradient id="gy" x1="0" y1="0" x2="0" y2="1"><stop offset="0" stop-color="#f9d84a"/><stop offset="1" stop-color="#f0a91c"/></linearGradient>
      <linearGradient id="go" x1="0" y1="0" x2="0" y2="1"><stop offset="0" stop-color="#f79a2a"/><stop offset="1" stop-color="#ea5a16"/></linearGradient>
      <linearGradient id="gl" x1="0" y1="0" x2="0" y2="1"><stop offset="0" stop-color="#d4ec3a"/><stop offset="1" stop-color="#8cc416"/></linearGradient>
      <linearGradient id="gt" x1="0" y1="0" x2="0" y2="1"><stop offset="0" stop-color="#8fe0c8"/><stop offset="1" stop-color="#46bfa5"/></linearGradient>
      <linearGradient id="gcy" x1="0" y1="0" x2="0" y2="1"><stop offset="0" stop-color="#4cc4ea"/><stop offset="1" stop-color="#1190cc"/></linearGradient>
      <linearGradient id="gb" x1="0" y1="0" x2="0" y2="1"><stop offset="0" stop-color="#4a95ea"/><stop offset="1" stop-color="#1a5cc8"/></linearGradient>
      <linearGradient id="gd" x1="0" y1="0" x2="0" y2="1"><stop offset="0" stop-color="#1d5ec8"/><stop offset="1" stop-color="#0a3596"/></linearGradient>
    </defs>
  </svg>

  <svg class="hex" style="left:290px;top:952px" width="140" height="158" viewBox="0 0 140 158"><polygon points="70,4 136,41 136,117 70,154 4,117 4,41" fill="url(#gy)" stroke="url(#gy)" stroke-width="6" stroke-linejoin="round"/><circle cx="70" cy="79" r="40" fill="#fff" stroke="#f3e6b6" stroke-width="4"/><rect x="58" y="62" width="24" height="32" rx="3" fill="none" stroke="var(--yellow)" stroke-width="2.5"/><circle cx="70" cy="74" r="6" fill="none" stroke="var(--yellow)" stroke-width="2"/></svg>
  <svg class="hex" style="left:290px;top:1115px" width="140" height="158" viewBox="0 0 140 158"><polygon points="70,4 136,41 136,117 70,154 4,117 4,41" fill="url(#go)" stroke="url(#go)" stroke-width="6" stroke-linejoin="round"/><circle cx="70" cy="79" r="40" fill="#fff" stroke="#f7d8bf" stroke-width="4"/><rect x="52" y="64" width="36" height="30" rx="3" fill="none" stroke="var(--orange)" stroke-width="2.5"/><line x1="52" y1="72" x2="88" y2="72" stroke="var(--orange)" stroke-width="2"/></svg>
  <svg class="hex" style="left:373px;top:1240px" width="140" height="158" viewBox="0 0 140 158"><polygon points="70,4 136,41 136,117 70,154 4,117 4,41" fill="url(#gl)" stroke="url(#gl)" stroke-width="6" stroke-linejoin="round"/><circle cx="70" cy="79" r="40" fill="#fff" stroke="#e5f2bd" stroke-width="4"/><rect x="52" y="68" width="36" height="22" rx="3" fill="none" stroke="var(--lime)" stroke-width="2.5"/><path d="M60 79h16l-5-5M76 79l-5 5" fill="none" stroke="var(--lime)" stroke-width="2"/></svg>
  <svg class="hex" style="left:524px;top:1302px" width="140" height="158" viewBox="0 0 140 158"><polygon points="70,4 136,41 136,117 70,154 4,117 4,41" fill="url(#gt)" stroke="url(#gt)" stroke-width="6" stroke-linejoin="round"/><circle cx="70" cy="79" r="40" fill="#fff" stroke="#d3f1e8" stroke-width="4"/><circle cx="70" cy="79" r="20" fill="none" stroke="var(--teal)" stroke-width="2.5" stroke-dasharray="4 3"/></svg>
  <svg class="hex" style="left:674px;top:1240px" width="140" height="158" viewBox="0 0 140 158"><polygon points="70,4 136,41 136,117 70,154 4,117 4,41" fill="url(#gcy)" stroke="url(#gcy)" stroke-width="6" stroke-linejoin="round"/><circle cx="70" cy="79" r="40" fill="#fff" stroke="#c6e8f4" stroke-width="4"/><rect x="58" y="62" width="24" height="34" rx="4" fill="none" stroke="var(--cyan)" stroke-width="2.5"/><text x="70" y="78" text-anchor="middle" font-family="Exo 2,sans-serif" font-size="9" font-weight="700" fill="var(--cyan)">VIP</text></svg>
  <svg class="hex" style="left:761px;top:1113px" width="140" height="158" viewBox="0 0 140 158"><polygon points="70,4 136,41 136,117 70,154 4,117 4,41" fill="url(#gb)" stroke="url(#gb)" stroke-width="6" stroke-linejoin="round"/><circle cx="70" cy="79" r="40" fill="#fff" stroke="#cfe0f6" stroke-width="4"/><rect x="54" y="76" width="16" height="16" fill="none" stroke="var(--blue)" stroke-width="2.5"/><rect x="70" y="76" width="16" height="16" fill="none" stroke="var(--blue)" stroke-width="2.5"/><rect x="62" y="60" width="16" height="16" fill="none" stroke="var(--blue)" stroke-width="2.5"/></svg>
  <svg class="hex" style="left:761px;top:950px" width="140" height="158" viewBox="0 0 140 158"><polygon points="70,4 136,41 136,117 70,154 4,117 4,41" fill="url(#gd)" stroke="url(#gd)" stroke-width="6" stroke-linejoin="round"/><circle cx="70" cy="79" r="40" fill="#fff" stroke="#c7d3ec" stroke-width="4"/><circle cx="70" cy="72" r="9" fill="none" stroke="var(--royal)" stroke-width="2.5"/><path d="M52 90c10 6 26 6 36-4" fill="none" stroke="var(--royal)" stroke-width="2.5"/></svg>

  <div class="svc r" style="left:91px;top:990px"><h3 style="color:var(--yellow)">Visa Services</h3>Lorem ipsum dolor sit amet consectetur adipiscing elit, sed do eiusmod tempor</div>
  <div class="svc r" style="left:91px;top:1143px"><h3 style="color:var(--orange)">International<br>Hotel Reservation</h3>Lorem ipsum dolor sit amet consectetur adipiscing elit, sed do eiusmod tempor</div>
  <div class="svc r" style="left:175px;top:1286px"><h3 style="color:var(--lime)">Worldwide Flight<br>Tickets Booking</h3>Lorem ipsum dolor sit amet consectetur adipiscing elit, sed do eiusmod tempor</div>
  <div class="svc c" style="left:510px;top:1470px"><h3 style="color:var(--teal)">Worldwide Travel<br>Arrangement</h3>Lorem ipsum dolor sit amet consectetur adipiscing elit, sed do eiusmod tempor</div>
  <div class="svc" style="left:830px;top:1290px"><h3 style="color:var(--cyan)">VIP Airport Concierge</h3>Lorem ipsum dolor sit amet consectetur adipiscing elit, sed do eiusmod tempor</div>
  <div class="svc" style="left:917px;top:1160px"><h3 style="color:var(--blue)">Duty Free Goods</h3>Lorem ipsum dolor sit amet consectetur adipiscing elit, sed do eiusmod tempor</div>
  <div class="svc" style="left:917px;top:980px"><h3 style="color:var(--royal)">International<br>Business Resources</h3>Lorem ipsum dolor sit amet consectetur adipiscing elit, sed do eiusmod tempor</div>
</section>

<section class="about">
  <div class="ring" style="left:126px;top:98px;width:422px;height:422px;border-color:#f0a040"></div>
  <div class="ring" style="left:130px;top:102px;width:420px;height:420px;border-color:#7ec65a"></div>
  <div class="ring" style="left:128px;top:103px;width:420px;height:420px;border-color:#2a6bd0"></div>
  <div class="about-photo" role="img" aria-label="Business traveller pulling a suitcase through a hotel lobby"></div>
  <h2>ABOUT PELICAN<br><span class="grad-text">GLOBAL FORUM</span></h2>
  <p>Lorem ipsum dolor sit amet, consectetur adipiscing elit, sed do eiusmod tempor incididunt ut labore et dolore magna aliqua. Quis ipsum susisse ultrices gravida. Risus commodo viverra maecenas accumsan lacus vel facilisis. Lorem ipsum dolor sit amet, consectetur adipiscing elit, sed do eiusmod tempor incididunt ut labore et dolore magna aliqua. Quis ipsum suspendisse ultrices gravida. Risus commodo viverra maecenas accumsan lacus vel facilisis. Lorem ipsum dolor sit amet, consectetur adipiscing elit, sed do eiusmod tempor incididunt ut labore et dolore magna aliqua. Quis ipsum suspendisse ultrices gravida.</p>
  <a class="btn">READ MORE</a>
</section>

<section class="news">
  <h2 class="section-title" style="top:2382px">PELICAN <span class="grad-text">NEWS</span></h2>
  <article class="card" style="left:44px">
    <div class="card-photo" role="img" aria-label="Traveller stretching by a sunlit hotel room window" style="background:linear-gradient(135deg,#f5d9a0,#c98a4a 55%,#6b4a35)"></div>
    <h4>Lorem ipsum dolor sit amlore cons ectetur adipiscing</h4>
    <p>Lorem ipsum dolor sit amet, consectetur adi piscing elit, sed do eiusmod tempor.</p>
    <span class="date">Apr 15 2023</span>
  </article>
  <article class="card" style="left:421px">
    <div class="card-photo" role="img" aria-label="Business passenger working on a laptop in an aircraft cabin" style="background:linear-gradient(135deg,#c9ced6,#8e949e 55%,#4b4f58)"></div>
    <h4>Lorem ipsum dolor sit amlore cons ectetur adipiscing</h4>
    <p>Lorem ipsum dolor sit amet, consectetur adi piscing elit, sed do eiusmod tempor.</p>
    <span class="date">Apr 15 2023</span>
  </article>
  <article class="card" style="left:798px">
    <div class="card-photo" role="img" aria-label="Family with luggage walking toward an airliner on the tarmac" style="background:linear-gradient(180deg,#dfe7ef,#c3ccd6 55%,#8a8f95)"></div>
    <h4>Lorem ipsum dolor sit amlore cons ectetur adipiscing</h4>
    <p>Lorem ipsum dolor sit amet, consectetur adi piscing elit, sed do eiusmod tempor.</p>
    <span class="date">Apr 15 2023</span>
  </article>
</section>

<section class="cities">
  <h2>OUR BUSINESS<br><span class="grad-text">RESOURCES CITIES</span></h2>
  <p>Lorem ipsum dolor sit amet, consectetur adipiscing elit, sed do eiusmod tempor incididunt ut labore et dolore magna aliqua. Quis ipsum suspendisse ultrices gravida. Risus commodo viverra maecenas accumsan lacus vel facilisis.</p>
  <div class="world-map" role="img" aria-label="World map marking business resource cities across the Americas, Europe, Africa, Asia and Australia"></div>
</section>

<footer class="footer">
  <div style="position:absolute;left:140px;top:150px;width:220px;text-align:center;font-family:'Exo 2',sans-serif;font-weight:700;font-size:18px;line-height:22px;color:var(--navy)">
    <div style="width:44px;height:44px;border-radius:50%;background:var(--navy);margin:0 auto 12px"></div>
    Pelican Global Trade &amp; Heritage Forum
  </div>
  <div class="vline" style="left:367px"></div>
  <div class="vline" style="left:517px"></div>
  <div class="vline" style="left:785px"></div>

  <h5 style="left:412px;top:82px">Links</h5>
  <ul class="flinks">
    <li>Home</li><li>About Us</li><li>Services</li><li>Cities</li><li>News</li><li>Contact Us</li>
  </ul>

  <h5 style="left:549px;top:82px">Contact</h5>
  <div class="contact-row" style="top:122px">
    <span class="ic"><svg width="14" height="18" viewBox="0 0 14 18"><path d="M7 1a6 6 0 0 0-6 6c0 4.5 6 10 6 10s6-5.5 6-10a6 6 0 0 0-6-6z" fill="#fff"/><circle cx="7" cy="7" r="2.2" fill="var(--btn)"/></svg></span>
    <div style="padding-top:6px">Address: ingo Lorem 677<br>Lorem ipsum dumys</div>
  </div>
  <div class="contact-row" style="top:176px">
    <span class="ic"><svg width="16" height="16" viewBox="0 0 16 16"><path d="M3 1l3 3-1.5 2a9 9 0 0 0 5.5 5.5L12 10l3 3-2 2C7 15 1 9 1 3z" fill="#fff"/></svg></span>
    <div style="padding-top:6px">Phone:<br>(09) 555 0142</div>
  </div>
  <div class="contact-row" style="top:230px">
    <span class="ic"><svg width="16" height="12" viewBox="0 0 16 12"><rect width="16" height="12" rx="1.5" fill="#fff"/><path d="M1 1l7 5 7-5" fill="none" stroke="var(--btn)" stroke-width="1.5"/></svg></span>
    <div style="padding-top:6px">Email:<br>info@pelicanforum.com</div>
  </div>

  <h5 style="left:825px;top:82px">Newsleter Sign up</h5>
  <div class="news-txt">Lorem ipsum dolor sit amet locon sectetur adipiscing elit.</div>
  <div class="email">Email:</div>
  <a class="btn signup">SIGN UP</a>

  <div class="hline"></div>
  <div class="copy">Copyright © 2023&nbsp; All rights reserved.</div>
</footer>

</body>
</html>
```